PELTON RIDGE HEATING AND COOLING

Industry/Entity Type

Hvac

Requirements
Must have
• logo
My name: Doug Ferriblen
Phone number 555-304-9461
Text:
Furnace and AC repairs
New furnace and AC installation
Ductwork
Gas lines
Water Tanks
Tankless water heaters
Nice to have
• Profesional modern look

```html
<!DOCTYPE html>
<html lang="en">
<head>
<meta charset="utf-8">
<title>Pelton Ridge Heating and Cooling – Business Card</title>
<link href="https://fonts.googleapis.com/css2?family=Fira+Sans:wght@400;500&display=swap" rel="stylesheet">
<style>
  :root {
    --page-green: #0b8b62;
    --card-dark: #1b1b1b;
    --card-dark-soft: #2b2b2b;
    --accent-red: #f41b3e;
    --brand-blue: #1c5fb3;
    --call-blue: #a9c6ef;
    --rule-cyan: #10e6f2;
    --rule-grey: #9a9a9a;
    --text-light: #f2f2f2;
    --text-dark: #111111;
    --paper-white: #ffffff;
  }
  * { box-sizing: border-box; margin: 0; padding: 0; }
  html, body {
    width: 1200px; height: 1000px; overflow: hidden;
    background: var(--page-green);
    font-family: "Fira Sans", Arial, sans-serif;
  }
  .canvas {
    position: relative; width: 1200px; height: 1000px;
    display: flex; flex-direction: column; align-items: center;
    justify-content: center; gap: 40px;
  }
  .card {
    position: relative; width: 780px; height: 446px; overflow: hidden;
    background: radial-gradient(ellipse at 55% 55%, var(--card-dark-soft) 0%, var(--card-dark) 70%);
  }
  .card-shapes { position: absolute; inset: 0; width: 100%; height: 100%; }

  /* Front */
  .front-brand {
    position: absolute; left: 0; right: 0; top: 62px;
    display: flex; flex-direction: column; align-items: center;
  }
  .brand-dot {
    width: 96px; height: 96px; border-radius: 50%;
    background: var(--brand-blue); margin-bottom: 26px;
  }
  .front-name {
    font-weight: 500; font-size: 58px; line-height: 1;
    letter-spacing: 1px; color: var(--brand-blue);
  }
  .front-tagline {
    margin-top: 12px; display: flex; align-items: center; gap: 10px;
    font-weight: 500; font-size: 21px; color: var(--brand-blue);
    letter-spacing: 0.5px;
  }
  .front-tagline::before, .front-tagline::after {
    content: ""; width: 56px; height: 2px; background: var(--rule-grey);
  }
  .front-call {
    position: absolute; top: 348px; left: 0; right: 0; text-align: center;
    font-size: 45px; line-height: 54px; color: var(--call-blue);
  }

  /* Back */
  .back-brand {
    position: absolute; top: 38px; left: 0; right: 0;
    display: flex; align-items: center; justify-content: center; gap: 14px;
    color: var(--text-light);
  }
  .back-brand .brand-dot { width: 40px; height: 40px; margin: 0; background: var(--text-light); }
  .back-brand-text { display: flex; flex-direction: column; }
  .back-name { font-weight: 500; font-size: 32px; line-height: 1; letter-spacing: 1px; }
  .back-tagline { font-weight: 500; font-size: 13px; letter-spacing: 0.5px; margin-top: 4px; }
  .service-list {
    position: absolute; top: 124px; left: 80px; width: 640px;
    list-style: none; display: grid;
    grid-template-columns: 396px auto; grid-auto-flow: column;
    grid-template-rows: repeat(3, 59px);
    font-size: 22px; color: var(--text-light); letter-spacing: 0.5px;
  }
  .owner {
    position: absolute; top: 326px; left: 0; right: 0; text-align: center;
    color: var(--text-dark);
  }
  .owner-name { font-size: 40px; line-height: 52px; letter-spacing: 0.5px; }
  .owner-phone {
    display: flex; align-items: center; justify-content: center; gap: 44px;
    font-size: 43px; line-height: 54px; margin-left: -30px;
  }
  .phone-icon { width: 52px; height: 38px; }
</style>
</head>
<body>
<main class="canvas">

  <section class="card card-front" aria-label="Card front">
    <svg class="card-shapes" viewBox="0 0 780 446" aria-hidden="true">
      <polygon points="685,0 780,0 780,95" fill="var(--accent-red)"/>
      <rect x="0" y="529" width="0" height="0"/>
      <rect x="0" y="373" width="172" height="5" fill="var(--rule-cyan)"/>
      <rect x="608" y="373" width="172" height="5" fill="var(--rule-cyan)"/>
    </svg>
    <div class="front-brand">
      <div class="brand-dot"></div>
      <div class="front-name">PELTON RIDGE</div>
      <div class="front-tagline">HEATING AND COOLING</div>
    </div>
    <p class="front-call">Call 555-304-9461</p>
  </section>

  <section class="card card-back" aria-label="Card back">
    <svg class="card-shapes" viewBox="0 0 780 446" aria-hidden="true">
      <polygon points="681,0 780,0 780,99" fill="var(--accent-red)"/>
      <path d="M0,322 C220,282 500,280 700,300 C460,296 220,312 0,352 Z" fill="var(--accent-red)"/>
      <path d="M0,352 C250,300 560,292 780,348 L780,446 L0,446 Z" fill="var(--paper-white)"/>
    </svg>
    <div class="back-brand">
      <div class="brand-dot"></div>
      <div class="back-brand-text">
        <span class="back-name">PELTON RIDGE</span>
        <span class="back-tagline">HEATING AND COOLING</span>
      </div>
    </div>
    <ul class="service-list">
      <li>Furnace and AC repairs</li>
      <li>New furnace &amp; AC installation</li>
      <li>Ductwork</li>
      <li>Gas lines</li>
      <li>Water Tanks</li>
      <li>Tankless water heaters</li>
    </ul>
    <div class="owner">
      <p class="owner-name">Doug Ferriblen</p>
      <p class="owner-phone">
        <svg class="phone-icon" viewBox="0 0 52 38" role="img" aria-label="Phone">
          <path d="M2,12 C2,2 50,2 50,12 L50,15 L38,15 L38,10 C32,8 20,8 14,10 L14,15 L2,15 Z" fill="var(--text-dark)"/>
          <path d="M12,16 L40,16 L48,30 L48,37 L4,37 L4,30 Z" fill="var(--text-dark)"/>
          <circle cx="26" cy="27" r="6" fill="var(--paper-white)"/>
          <circle cx="26" cy="27" r="2.5" fill="var(--text-dark)"/>
        </svg>
        <span>555-304-9461</span>
      </p>
    </div>
  </section>

</main>
</body>
</html>
```